Marketing Flyer for Plumber Referals

8.5" x11" Layout should be landscape not portrait. Create a bold, eye-catching flyer that highlights earning potential from referrals for water damage restoration. Use high-contrast colors like blue, yellow, and white, with bold fonts and dynamic layouts. Include images of restoration work, cash, and happy clients. Emphasize key benefits like $500 minimum payouts, fast payments, and unlimited income potential. Keep instructions simple: refer a client, we handle the work, you get paid. Add a clear call-to-action and display contact details prominently. Focus on professionalism and energy.

Target Market(s)

Plumbers and Contractor 8.5" x11" Layout should be landscape not portrait.

Industry/Entity Type

General Contractor

Colors
0054AA
0677BA
7BADD7
CADEEF
E8F1F8
EB3D1F
EC4F4E
F09395
F8D3D4
FCEDEE

Requirements
Must have
• 8.5" x11" Layout should be landscape not portrait.
Nice to have

```html
<!DOCTYPE html>
<html lang="en">
<head>
<meta charset="utf-8">
<title>Get Paid to Refer a Flood – Referral Flyer</title>
<link href="https://fonts.googleapis.com/css2?family=Montserrat:ital,wght@0,600;0,700;0,800;0,900;1,800;1,900&family=Oswald:wght@600;700&display=swap" rel="stylesheet">
<style>
:root{
  --blue-deep:#0054AA;
  --blue:#0677BA;
  --blue-mid:#1a6fc4;
  --blue-soft:#7BADD7;
  --blue-pale:#CADEEF;
  --blue-mist:#E8F1F8;
  --yellow:#FFD21F;
  --white:#ffffff;
  --ink:#0c1e3a;
  --stage:#8f8f8f;
}
*{box-sizing:border-box;margin:0;padding:0}
html,body{width:1200px;height:2324px;overflow:hidden}
body{background:var(--stage);font-family:'Montserrat',Arial,sans-serif;color:var(--white);position:relative}
.flyer{position:absolute;left:60px;width:1080px;height:835px;overflow:hidden;box-shadow:0 10px 30px rgba(0,0,0,.35)}
.flyer--front{top:297px;background:var(--blue-deep)}
.flyer--back{top:1192px;background:var(--blue)}

/* FRONT */
.front__photo{position:absolute;right:0;top:0;width:600px;height:725px;background:linear-gradient(180deg,#a68bc4 0%,#d9a9b8 35%,#6f8fb4 70%,#44566e 100%)}
.front__panel{position:absolute;left:0;top:0;width:580px;height:725px;background:linear-gradient(160deg,var(--blue-mid),var(--blue-deep));padding:30px 0 0 36px;z-index:2;clip-path:polygon(0 0,100% 0,92% 100%,0 100%)}
.headline-top{display:flex;align-items:flex-start;gap:18px}
.headline-earn{font:italic 900 64px/0.95 'Montserrat',sans-serif;color:var(--yellow)}
.headline-unlimited{font:italic 900 26px/1 'Montserrat',sans-serif;color:var(--yellow);margin-top:2px}
.headline-cash{font:italic 900 64px/0.95 'Montserrat',sans-serif;color:var(--white)}
.headline-refer{font:italic 900 46px/1.02 'Montserrat',sans-serif;color:var(--white);margin-top:8px}
.headline-refer span{color:var(--yellow)}
.pills{margin-top:16px;display:flex;flex-direction:column;gap:10px}
.pill{display:flex;align-items:center;gap:12px;background:var(--yellow);color:var(--ink);font:800 16px/1.15 'Montserrat',sans-serif;padding:8px 14px;width:470px;border-radius:4px}
.pill svg{flex:none}
.why-title{font:900 26px/1 'Montserrat',sans-serif;margin:20px 0 12px}
.benefit{display:flex;gap:14px;align-items:flex-start;margin-bottom:10px;width:450px}
.benefit__icon{flex:none;width:38px;height:38px;border-radius:50%;background:var(--yellow);display:flex;align-items:center;justify-content:center}
.benefit__name{font:800 15px/1.1 'Montserrat',sans-serif;color:var(--yellow)}
.benefit__text{font:600 12px/1.3 'Montserrat',sans-serif;color:var(--blue-mist)}
.front__inset{position:absolute;left:600px;top:400px;width:240px;height:150px;border:4px solid var(--white);background:linear-gradient(135deg,#c9c2b4,#7d8a98);z-index:3}
.front__tagline{position:absolute;left:0;bottom:0;width:100%;height:110px;background:var(--white);display:flex;align-items:center;justify-content:center;white-space:nowrap;font:700 50px/1 'Oswald',sans-serif;color:var(--ink)}
.front__tagline span{color:var(--blue);margin:0 .3em}

/* BACK */
.back__skyline{position:absolute;inset:0;background:linear-gradient(180deg,var(--blue) 0%,#3b8fcf 35%,var(--blue-deep) 75%)}
.back__content{position:relative;text-align:center;padding-top:34px}
.back__title{font:900 70px/1.02 'Montserrat',sans-serif;color:var(--white)}
.back__sub{font:800 34px/1 'Montserrat',sans-serif;color:var(--yellow);margin-top:12px}
.steps{display:flex;justify-content:center;gap:40px;margin-top:24px}
.step{width:300px}
.step__num{width:58px;height:58px;border-radius:50%;background:var(--yellow);color:var(--ink);font:900 32px/58px 'Montserrat',sans-serif;margin:0 auto 10px}
.step__name{font:800 18px/1.2 'Montserrat',sans-serif}
.step__text{font:600 13px/1.35 'Montserrat',sans-serif;color:var(--blue-mist);margin-top:6px}
.gallery{position:absolute;left:0;top:500px;width:100%;height:215px;display:flex}
.gallery__item{flex:1;border-right:4px solid var(--white)}
.gallery__item:last-child{border-right:none}
.gallery__item--a{background:linear-gradient(135deg,#d7d2c8,#8b8f95)}
.gallery__item--b{background:linear-gradient(135deg,#e3e6ea,#9aa9b8)}
.gallery__item--c{background:linear-gradient(135deg,#b9b2a2,#5e6a78)}
.back__contact{position:absolute;left:0;bottom:0;width:100%;height:120px;background:var(--white);display:flex;align-items:center;padding:0 40px;gap:50px;color:var(--ink)}
.cta{font:900 26px/1.05 'Montserrat',sans-serif;color:var(--ink)}
.cta small{display:block;font:800 20px/1 'Montserrat',sans-serif;color:var(--blue)}
.contact-item{display:flex;align-items:center;gap:12px;font:800 32px/1 'Montserrat',sans-serif}
.contact-item--web{font-size:24px;font-weight:700}
.contact-item__icon{width:46px;height:46px;border-radius:50%;background:var(--blue);display:flex;align-items:center;justify-content:center}
</style>
</head>
<body>

<section class="flyer flyer--front">
  <div class="front__photo" role="img" aria-label="City skyline at dusk with a smiling client giving a thumbs up"></div>
  <div class="front__panel">
    <div class="headline-top">
      <div><div class="headline-earn">EARN</div><div class="headline-unlimited">UNLIMITED</div></div>
      <div class="headline-cash">CASH</div>
    </div>
    <div class="headline-refer">GET PAID TO<br>REFER A <span>FLOOD</span></div>
    <div class="pills">
      <div class="pill"><svg width="18" height="18" viewBox="0 0 20 20"><path d="M3 10l5 5 9-10" stroke="#0c1e3a" stroke-width="3" fill="none"/></svg>$500 Minimum or 10% Per Referral</div>
      <div class="pill"><svg width="18" height="18" viewBox="0 0 20 20"><path d="M3 10l5 5 9-10" stroke="#0c1e3a" stroke-width="3" fill="none"/></svg>Partner with the #1 Water Damage Restoration Team</div>
    </div>
    <div class="why-title">Why Partner with Us?</div>
    <div class="benefit"><div class="benefit__icon"><svg width="20" height="20" viewBox="0 0 22 22"><path d="M4 11l5 5 9-10" stroke="#0054AA" stroke-width="3" fill="none"/></svg></div><div><div class="benefit__name">Guaranteed Payout</div><div class="benefit__text">Earn a minimum of $500 or 10% on every job we close.</div></div></div>
    <div class="benefit"><div class="benefit__icon"><svg width="20" height="20" viewBox="0 0 22 22"><circle cx="11" cy="11" r="8" stroke="#0054AA" stroke-width="3" fill="none"/><path d="M11 6v5l3 3" stroke="#0054AA" stroke-width="2.5" fill="none"/></svg></div><div><div class="benefit__name">Fast Estimations</div><div class="benefit__text">Quick on-site estimates so your client gets answers the same day.</div></div></div>
    <div class="benefit"><div class="benefit__icon"><svg width="20" height="20" viewBox="0 0 22 22"><path d="M11 2l2.6 6 6.4.5-4.9 4.2 1.5 6.3L11 15.6 5.4 19l1.5-6.3L2 8.5 8.4 8z" fill="#0054AA"/></svg></div><div><div class="benefit__name">Industry Leaders</div><div class="benefit__text">Certified crews trusted across the region for 24/7 water restoration.</div></div></div>
    <div class="benefit"><div class="benefit__icon"><svg width="20" height="20" viewBox="0 0 22 22"><path d="M11 3c-3 4-6 7-6 10a6 6 0 0012 0c0-3-3-6-6-10z" fill="#0054AA"/></svg></div><div><div class="benefit__name">Affordable Solutions</div><div class="benefit__text">Fair, transparent pricing that keeps your customers coming back.</div></div></div>
  </div>
  <div class="front__inset" role="img" aria-label="Restoration equipment drying a water-damaged room"></div>
  <div class="front__tagline">Send Referrals.<span>Get Paid.</span>Grow Your Business.</div>
</section>

<section class="flyer flyer--back">
  <div class="back__skyline" role="img" aria-label="Faded city skyline in blue tones"></div>
  <div class="back__content">
    <h1 class="back__title">GET PAID TO<br>REFER A FLOOD</h1>
    <div class="back__sub">How It Works</div>
    <div class="steps">
      <div class="step"><div class="step__num">1</div><div class="step__name">Refer Flood, Water and Mold Damage</div><div class="step__text">Call, text, book online, or send us photos.</div></div>
      <div class="step"><div class="step__num">2</div><div class="step__name">We Take Care of Everything</div><div class="step__text">Free estimates, insurance claims, and full professional service.</div></div>
      <div class="step"><div class="step__num">3</div><div class="step__name">Get Paid Fast</div><div class="step__text">$500 minimum or 10% of the invoice within 48 hours of final payment.</div></div>
    </div>
  </div>
  <div class="gallery">
    <div class="gallery__item gallery__item--a" role="img" aria-label="Technician repairing water-damaged drywall"></div>
    <div class="gallery__item gallery__item--b" role="img" aria-label="Crew member inspecting a ceiling for moisture"></div>
    <div class="gallery__item gallery__item--c" role="img" aria-label="Worker removing damaged flooring"></div>
  </div>
  <div class="back__contact">
    <div class="cta">CALL TEXT OR<small>BOOK ON-LINE</small></div>
    <div class="contact-item"><span class="contact-item__icon"><svg width="24" height="24" viewBox="0 0 24 24"><path d="M6 2l4 4-2 3c1 3 4 6 7 7l3-2 4 4-3 4C10 22 2 14 2 5z" fill="#fff"/></svg></span>555-014-2290</div>
    <div class="contact-item contact-item--web"><span class="contact-item__icon"><svg width="24" height="24" viewBox="0 0 24 24"><circle cx="12" cy="12" r="9" stroke="#fff" stroke-width="2" fill="none"/><path d="M3 12h18M12 3c3 3 3 15 0 18M12 3c-3 3-3 15 0 18" stroke="#fff" stroke-width="1.6" fill="none"/></svg></span>BrightHarborRestore.com</div>
  </div>
</section>

</body>
</html>
```